Deactivated Coal-Fired Power Plant to be redeveloped into a Green Energy Campus.

Want a striking business card statement that introduces our concept project to provide economic and community recovery to a former rural coal community in western PA.
Essentially 12 project representatives that will lead both the demolition of an existing power plant and the redevelopment to a new Green energy site.
Business Card should reflect our effort.
We are open to ideas.

Target Market(s)

Energy and Power Generation industries

Industry/Entity Type

Power Generation and Data Centers

Contact Information for Business Card

Included in uploaded materials

Font styles to use
Sans Serif
Other font styles liked:
• Arial, Calibri

Requirements
Must have
• Multiple colors

```html
<!DOCTYPE html>
<html lang="en">
<head>
<meta charset="utf-8">
<title>Ridgeline Renewal – Business Card</title>
<link rel="stylesheet" href="https://fonts.googleapis.com/css2?family=Lato:wght@400;700&family=Roboto:wght@500&display=swap">
<style>
  :root {
    --backdrop: #8a8a8a;
    --card-paper: #efefef;
    --brand-green: #1f9a47;
    --ink: #151515;
    --photo-sky: #5b6464;
    --photo-hills: #3d4d3a;
    --photo-ground: #2f4229;
    --white: #ffffff;
  }
  * { margin: 0; padding: 0; box-sizing: border-box; }
  html, body {
    width: 1200px;
    height: 781px;
    overflow: hidden;
    background: var(--backdrop);
  }
  .canvas {
    position: relative;
    width: 1200px;
    height: 781px;
  }
  .card {
    position: absolute;
    left: 355px;
    width: 456px;
    height: 259px;
    overflow: hidden;
  }
  .card--front {
    top: 98px;
    background: var(--card-paper);
  }
  .card--back {
    top: 399px;
  }

  /* Wordmark */
  .wordmark {
    position: absolute;
    display: flex;
    align-items: center;
    gap: 7px;
    font-family: "Lato", Arial, sans-serif;
    font-weight: 700;
    letter-spacing: 0.02em;
    line-height: 1.05;
    text-transform: uppercase;
  }
  .wordmark__dot {
    flex: none;
    border-radius: 50%;
    background: var(--brand-green);
  }
  .card--front .wordmark {
    left: 26px;
    top: 50px;
    font-size: 17px;
    color: var(--ink);
  }
  .card--front .wordmark__dot { width: 30px; height: 30px; }
  .card--back .wordmark {
    left: 50%;
    top: 50%;
    transform: translate(-50%, -50%);
    font-size: 22px;
    color: var(--white);
  }
  .card--back .wordmark__dot { width: 38px; height: 38px; }

  /* Contact block */
  .contact {
    position: absolute;
    left: 213px;
    top: 129px;
    font-family: "Lato", Arial, sans-serif;
    color: var(--ink);
  }
  .contact__name {
    font-family: "Roboto", Arial, sans-serif;
    font-weight: 500;
    font-size: 16px;
    color: var(--brand-green);
    line-height: 1.2;
  }
  .contact__role {
    font-size: 10.5px;
    line-height: 1.3;
    margin-bottom: 15px;
  }
  .contact__list { list-style: none; }
  .contact__item {
    display: flex;
    align-items: center;
    gap: 5px;
    font-size: 10.5px;
    height: 15px;
  }
  .contact__icon {
    width: 9px;
    height: 9px;
    flex: none;
    fill: var(--brand-green);
  }
  .contact__domain { color: var(--brand-green); }

  /* Back photo area */
  .site-photo {
    position: absolute;
    inset: 0;
    background: linear-gradient(180deg, var(--photo-sky) 0%, var(--photo-hills) 22%, var(--photo-ground) 100%);
  }
</style>
</head>
<body>
<main class="canvas">
  <section class="card card--front">
    <div class="wordmark">
      <span class="wordmark__dot"></span>
      <span>Ridgeline<br>Renewal</span>
    </div>

    <div class="contact">
      <h1 class="contact__name">Daniel Moreau</h1>
      <p class="contact__role">Chief Operating Officer</p>
      <ul class="contact__list">
        <li class="contact__item">
          <svg class="contact__icon" viewBox="0 0 10 10"><path d="M2.2 0.5 L3.6 2.6 L2.7 3.6 Q3.6 5.6 6.4 7.3 L7.4 6.4 L9.5 7.8 L8.5 9.5 Q4.5 9.3 1.6 5.6 Q0.3 3.6 0.5 1.5 Z"/></svg>
          <span>555-014-2000</span>
        </li>
        <li class="contact__item">
          <svg class="contact__icon" viewBox="0 0 10 10"><path d="M2.5 0 H7.5 V10 H2.5 Z M3.4 1 V8 H6.6 V1 Z M4.5 8.5 H5.5 V9.3 H4.5 Z"/></svg>
          <span>555-014-9999 (Office)</span>
        </li>
        <li class="contact__item">
          <svg class="contact__icon" viewBox="0 0 10 10"><path d="M0 2 H10 V3 L5 6 L0 3 Z M0 4 L5 7 L10 4 V8.5 H0 Z"/></svg>
          <span>dmoreau@ridgelinerenewal.com</span>
        </li>
        <li class="contact__item">
          <svg class="contact__icon" viewBox="0 0 10 10"><circle cx="5" cy="5" r="4.3" fill="none" stroke="var(--brand-green)" stroke-width="1"/><ellipse cx="5" cy="5" rx="1.8" ry="4.3" fill="none" stroke="var(--brand-green)" stroke-width="0.8"/><path d="M0.7 5 H9.3" stroke="var(--brand-green)" stroke-width="0.8"/></svg>
          <span>www.<span class="contact__domain">ridgelinerenewal</span>.com</span>
        </li>
      </ul>
    </div>
  </section>

  <section class="card card--back">
    <div class="site-photo" role="img" aria-label="Aerial photograph of the power plant site with smokestacks among green rolling hills"></div>
    <div class="wordmark">
      <span class="wordmark__dot"></span>
      <span>Ridgeline<br>Renewal</span>
    </div>
  </section>
</main>
</body>
</html>
```